Pages That Sell Services - book cover (front panel only)

I want a book cover (for print and ebook) in a distinctive, quirky style that can be repurposed for podcast artwork too. Full brief supplied.
The book is a practical, accessible handbook for anyone thinking about writing a book to build their business, with a wide range of tips and techniques to help plan, write, publishing and promote a book that’s integrated with your platform and works to build your reputation, network and credibility from day 1.
The target audience is experts in business, particularly owners of SMEs with an established online and offline platform (eg speaking, training, consulting) who want to add a book to take their business to the next level.
I want the design to be strong and distinctive, slightly quirky without being gimmicky, with the focus on typography.

Target Market(s)

Those writing a book based on their expertise to build their business

Industry/Entity Type

Publishing Company

Font styles to use
Serif
Sans Serif
Decorative

Colors

Designer to choose colors to be used in the design.

Requirements
Must have
• Commercially appealing book cover design, with application files and copyright supplied, front panel only, 5.5 x 8.5 inch format. Must work at both full size and thumbnail.
Nice to have
• A distinctive style that could be applied across other products in my portfolio.

```html
<!DOCTYPE html>
<html lang="en">
<head>
<meta charset="utf-8">
<title>Pages That Sell Services — Front Cover</title>
<link rel="stylesheet" href="https://fonts.googleapis.com/css2?family=Anton&family=Montserrat:ital,wght@0,700;0,900;1,900&family=Oswald:wght@600&display=swap">
<style>
  :root {
    --paper-light: #ffffff;
    --paper-mid: #eeeeee;
    --paper-edge: #dadada;
    --title-purple: #8d2489;
    --title-plum: #4b0d3f;
    --banner-green: #abc23a;
    --banner-shade: #98ad2e;
    --subtitle-ink: #3a4210;
    --author-ink: #1e1e1e;
    --pen-dark: #151515;
    --pen-mid: #3b3b3b;
  }
  html, body {
    margin: 0;
    padding: 0;
    width: 776px;
    height: 1200px;
    overflow: hidden;
    background: var(--paper-mid);
  }
  .cover {
    position: relative;
    width: 776px;
    height: 1200px;
    overflow: hidden;
    background: radial-gradient(ellipse at 50% 45%, var(--paper-light) 0%, var(--paper-mid) 65%, var(--paper-edge) 100%);
  }
  .cover-art {
    position: absolute;
    inset: 0;
    width: 776px;
    height: 1200px;
  }
  .title-letter {
    font-family: "Montserrat", sans-serif;
    font-weight: 900;
    font-size: 100px;
    fill: var(--title-purple);
    stroke: var(--paper-light);
    stroke-width: 5;
    paint-order: stroke;
    text-anchor: middle;
  }
  .title-letter--lead { font-style: italic; }
  .title-key-letter {
    font-family: "Anton", sans-serif;
    font-size: 100px;
    fill: var(--title-plum);
    stroke: var(--paper-light);
    stroke-width: 7;
    paint-order: stroke;
    text-anchor: middle;
  }
  .banner { fill: var(--banner-green); }
  .banner-shade { fill: var(--banner-shade); }
  .subtitle {
    font-family: "Oswald", sans-serif;
    font-weight: 600;
    font-size: 33px;
    letter-spacing: 0.5px;
    fill: var(--subtitle-ink);
    text-anchor: middle;
  }
  .author {
    position: absolute;
    left: 0;
    right: 0;
    top: 1052px;
    margin: 0;
    line-height: 1;
    text-align: center;
    font-family: "Montserrat", sans-serif;
    font-weight: 700;
    font-size: 72px;
    letter-spacing: 3px;
    color: var(--author-ink);
  }
</style>
</head>
<body>
<main class="cover">
  <svg class="cover-art" viewBox="0 0 776 1200" xmlns="http://www.w3.org/2000/svg">
    <defs>
      <linearGradient id="pen-tone" x1="0" y1="0" x2="1" y2="0">
        <stop offset="0" stop-color="var(--pen-mid)"/>
        <stop offset="0.4" stop-color="var(--pen-dark)"/>
        <stop offset="1" stop-color="#050505"/>
      </linearGradient>
    </defs>

    <g class="title" aria-label="Pages That Sell Services">
      <g class="title-row title-row--one">
        <text class="title-letter title-letter--lead" transform="translate(268,160) rotate(-6) scale(0.95,1.12)">P</text>
        <text class="title-letter title-letter--lead" transform="translate(333,164) rotate(-3) scale(0.95,1.2)">A</text>
        <text class="title-letter title-letter--lead" transform="translate(398,167) scale(0.95,1.22)">G</text>
        <text class="title-letter title-letter--lead" transform="translate(463,171) rotate(3) scale(0.95,1.18)">E</text>
        <text class="title-letter title-letter--lead" transform="translate(524,176) rotate(6) scale(0.95,1.08)">S</text>
      </g>
      <g class="title-row title-row--two">
        <text class="title-letter" transform="translate(238,305) scale(1.3,1.5)">T</text>
        <text class="title-letter" transform="translate(338,303) scale(1.15,1.36)">H</text>
        <text class="title-letter" transform="translate(440,303) scale(1.15,1.36)">A</text>
        <text class="title-letter" transform="translate(538,305) scale(1.3,1.5)">T</text>
      </g>
      <g class="title-row title-row--three">
        <text class="title-letter" transform="translate(212,446) rotate(-7) scale(1.5,1.75)">S</text>
        <text class="title-letter" transform="translate(330,440) rotate(-2) scale(1.55,1.45)">E</text>
        <text class="title-letter" transform="translate(446,440) rotate(2) scale(1.6,1.45)">L</text>
        <text class="title-letter" transform="translate(562,446) rotate(7) scale(1.6,1.7)">L</text>
      </g>
      <g class="title-row title-row--key">
        <text class="title-key-letter" transform="translate(172,650) scale(1.25,1.72)">S</text>
        <text class="title-key-letter" transform="translate(235,665) scale(1.25,2.07)">E</text>
        <text class="title-key-letter" transform="translate(298,677) scale(1.25,2.36)">R</text>
        <text class="title-key-letter" transform="translate(361,685) scale(1.25,2.53)">V</text>
        <text class="title-key-letter" transform="translate(420,685) scale(1.25,2.53)">I</text>
        <text class="title-key-letter" transform="translate(480,677) scale(1.25,2.36)">C</text>
        <text class="title-key-letter" transform="translate(543,665) scale(1.25,2.07)">E</text>
        <text class="title-key-letter" transform="translate(606,650) scale(1.25,1.72)">S</text>
      </g>
    </g>

    <g class="subtitle-banner">
      <polygon class="banner" points="148,735 622,745 612,995 214,995 182,1030 192,995 140,995"/>
      <polygon class="banner-shade" points="140,870 612,995 214,995 182,1030 192,995 140,995"/>
      <text class="subtitle" x="386" y="815">CLEVER WAYS TO PLAN</text>
      <text class="subtitle" x="386" y="860">AND WRITE A BOOK</text>
      <text class="subtitle" x="386" y="905">THAT WORKS HARDER</text>
      <text class="subtitle" x="386" y="950">FOR YOUR BUSINESS</text>
    </g>

    <rect class="pen-photo" role="img" aria-label="Photograph of a black and gold pen writing diagonally" x="-25" y="-410" width="50" height="820" fill="url(#pen-tone)" transform="translate(672,555) rotate(10)"/>
  </svg>

  <p class="author">MAREN COLBY</p>
</main>
</body>
</html>
```